Morvex Business Card (intended for Business Card sized magnet)

Hi guys,

I would like to get a design for my business card for the restaurant. The design must be single sided as I intend to produce business card sized magnets.

The File attached must me on and I'm open for new ides

Can you please ensure that the design meets Cardowell's magnetic business card size specifications:

http://www.cardowell.example.au/custom-magnets.aspx?txi=15695&xnid=TopNav_Magnetic+Business+Cards+(linked+item)_Magnets_Marketing+Products&xnav=TopNav

Full Bleed Size (starting document size):
90 x 52 mm
1062 x 615 pixels
* Finished artwork should use the full bleed dimensions for best results.

Document Trim Size (final size after being cut):
87 x 49 mm
1028 x 579 pixels
* Please be sure to keep all text within the safe margin.

Resolution:
300 DPI

The winning design/source files need to meet these specifications.

Thanks
Updates

Hi guys, can I see more options please Thanks

```html
<!DOCTYPE html>
<html lang="en">
<head>
<meta charset="utf-8">
<title>Morvex Business Card</title>
<link rel="stylesheet" href="https://fonts.googleapis.com/css2?family=Cardo&family=PT+Sans+Narrow&family=Short+Stack&display=swap">
<style>
  :root {
    --page: #ffffff;
    --card: #0f1111;
    --pattern-dark: #1a1c1d;
    --pattern-light: #34373a;
    --rule-grey: #8c8f91;
    --rule-white: #f4f4f4;
    --ink: #ffffff;
  }
  html, body {
    margin: 0;
    padding: 0;
    width: 1200px;
    height: 1000px;
    overflow: hidden;
    background: var(--page);
  }
  .card {
    position: absolute;
    left: 82px;
    top: 205px;
    width: 1021px;
    height: 590px;
    background: var(--card);
    overflow: hidden;
  }
  .ornament-strip {
    position: absolute;
    top: 0;
    width: 117px;
    height: 590px;
    border-left: 3px solid var(--rule-grey);
    border-right: 3px solid var(--rule-grey);
    background: linear-gradient(180deg, var(--pattern-light), var(--pattern-dark) 50%, var(--pattern-light));
  }
  .ornament-strip--left { left: 78px; }
  .ornament-strip--right { left: 821px; }
  .ornament-band {
    position: absolute;
    left: 0;
    top: 150px;
    width: 1021px;
    height: 123px;
    border-top: 3px solid var(--rule-grey);
    border-bottom: 3px solid var(--rule-grey);
    background: linear-gradient(90deg, var(--pattern-dark), var(--pattern-light) 50%, var(--pattern-dark));
  }
  .ornament-band__rule {
    position: absolute;
    left: 200px;
    width: 621px;
    height: 3px;
    background: var(--rule-white);
  }
  .ornament-band__rule--top { top: -3px; }
  .ornament-band__rule--bottom { bottom: -3px; }
  .brand-name {
    position: absolute;
    left: 0;
    width: 1021px;
    top: 12px;
    margin: 0;
    text-align: center;
    font-family: "Cardo", serif;
    font-weight: 400;
    font-size: 92px;
    line-height: 1.2;
    color: var(--ink);
  }
  .contact {
    position: absolute;
    left: 0;
    width: 1021px;
    top: 298px;
    margin: 0;
    text-align: center;
    color: var(--ink);
    font-style: normal;
    font-family: "PT Sans Narrow", sans-serif;
    font-size: 35px;
  }
  .contact__line {
    display: block;
    height: 51px;
    line-height: 51px;
  }
  .contact__phone {
    display: block;
    height: 56px;
    line-height: 56px;
    font-family: "Short Stack", cursive;
    font-size: 44px;
    letter-spacing: 4px;
  }
</style>
</head>
<body>
  <div class="card">
    <div class="ornament-strip ornament-strip--left" role="img" aria-label="Vertical band of interlaced geometric star pattern with coloured gem centres"></div>
    <div class="ornament-strip ornament-strip--right" role="img" aria-label="Vertical band of interlaced geometric star pattern with coloured gem centres"></div>
    <div class="ornament-band" role="img" aria-label="Horizontal band of interlaced eight-point stars with red, green and gold gem centres">
      <span class="ornament-band__rule ornament-band__rule--top"></span>
      <span class="ornament-band__rule ornament-band__rule--bottom"></span>
    </div>
    <h1 class="brand-name">Morvex</h1>
    <address class="contact">
      <span class="contact__line">412 Larkfield Rd.</span>
      <span class="contact__line">Brenmoor East VIC 3190</span>
      <span class="contact__phone">03 9481 2737</span>
      <span class="contact__line">www.morvex.com.au</span>
      <span class="contact__line">Morvex412@mailbox.example</span>
    </address>
  </div>
</body>
</html>
```